Ground breaking athletic gear company needs a kick ass business card

We are an American start up athletic gear company that uses a medically proven biohack to boost athletic performance. Heat kills strength and endurance. Our gear helps athletes manage heat better and ultimatley can improve them by up to 10% instantly. Nothing like it out there! Launching this summer.
We are looking for a modern, minimalist design that captures a sporty edge. Check out www.vanteluxgear.com, @vanteluxgear on pictorama for more ideas.

Target Market(s)

25-35 year olds, male and female athletes, vortexlift athletes, competitive runners

Industry/Entity Type

Business

Contact Information for Business Card

Derek Hollins
Founder
derekh@vanteluxgear.com
www.VanteluxGear.com
+1 (555) 014-2286

Font styles to use
Sans Serif

Requirements
Must have
• Logo and icon
• All contact information
• derekh@vanteluxgear.com
• +1 (555) 019-4431 M
• +1 (555) 014-2286
Nice to have
• Tag line : "Cool & Conquer"

```html
<!DOCTYPE html>
<html lang="en">
<head>
<meta charset="UTF-8">
<title>Vantelux Gear — Business Card</title>
<link href="https://fonts.googleapis.com/css2?family=Mulish:wght@400;600;700&display=swap" rel="stylesheet">
<style>
  :root {
    --page-bg: #1c1c1e;
    --card-dark: #222325;
    --card-mid: #2e2f32;
    --card-light: #3b3c40;
    --panel-light: #5a5c62;
    --text-white: #f2f3f5;
    --accent-blue: #3f6fb3;
  }
  * { margin: 0; padding: 0; box-sizing: border-box; }
  html, body {
    width: 1200px;
    height: 800px;
    overflow: hidden;
    background: var(--page-bg);
    font-family: "Mulish", sans-serif;
  }
  .stage {
    width: 1200px;
    height: 800px;
    display: flex;
    align-items: center;
    justify-content: center;
    gap: 50px;
  }
  .card {
    position: relative;
    width: 525px;
    height: 300px;
    border-radius: 3px;
    overflow: hidden;
    box-shadow: 0 10px 30px rgba(0,0,0,0.45);
  }
  .card-surface {
    position: absolute;
    inset: 0;
    background:
      linear-gradient(200deg, rgba(255,255,255,0.05) 0 30%, transparent 30% 100%),
      linear-gradient(140deg, transparent 0 55%, rgba(0,0,0,0.12) 55% 100%),
      radial-gradient(ellipse at 65% 30%, var(--card-light) 0%, transparent 60%),
      linear-gradient(135deg, var(--card-mid) 0%, var(--card-dark) 70%);
  }
  .feature-panel {
    position: absolute;
    left: 0;
    top: 0;
    width: 215px;
    height: 300px;
    background:
      linear-gradient(115deg, var(--panel-light) 0%, var(--card-light) 45%, transparent 100%);
    opacity: 0.55;
  }
  /* Front */
  .holder {
    position: absolute;
    left: 172px;
    top: 48px;
  }
  .holder-name {
    color: var(--text-white);
    font-weight: 700;
    font-size: 31px;
    letter-spacing: 0.2px;
    line-height: 1.1;
  }
  .holder-role {
    color: var(--accent-blue);
    font-weight: 600;
    font-size: 21px;
    line-height: 1.1;
  }
  .contact-list {
    position: absolute;
    left: 300px;
    top: 202px;
    list-style: none;
  }
  .contact-item {
    display: flex;
    align-items: center;
    gap: 10px;
    color: var(--text-white);
    font-size: 13.5px;
    font-weight: 600;
    line-height: 20px;
  }
  .contact-icon {
    width: 13px;
    height: 13px;
    flex: none;
  }
  /* Back */
  .brand {
    position: absolute;
    inset: 0;
    display: flex;
    align-items: center;
    justify-content: center;
    gap: 10px;
  }
  .brand-mark {
    width: 14px;
    height: 14px;
    background: var(--text-white);
  }
  .brand-name {
    color: var(--text-white);
    font-weight: 700;
    font-size: 22px;
    letter-spacing: 3px;
    text-transform: uppercase;
  }
</style>
</head>
<body>
  <main class="stage">
    <section class="card card-front" aria-label="Business card front">
      <div class="card-surface" role="img" aria-label="Dark faceted low-poly background"></div>
      <div class="feature-panel" role="img" aria-label="Large brand emblem area in white and grey tones"></div>
      <div class="holder">
        <p class="holder-name">Derek Hollins</p>
        <p class="holder-role">Founder</p>
      </div>
      <ul class="contact-list">
        <li class="contact-item">
          <svg class="contact-icon" viewBox="0 0 14 14" aria-hidden="true">
            <rect x="1" y="3" width="12" height="8" fill="none" stroke="#3f6fb3" stroke-width="1.4"/>
            <path d="M1 3 L7 8 L13 3" fill="none" stroke="#3f6fb3" stroke-width="1.4"/>
          </svg>
          derekh@vanteluxgear.com
        </li>
        <li class="contact-item">
          <svg class="contact-icon" viewBox="0 0 14 14" aria-hidden="true">
            <circle cx="7" cy="7" r="5.5" fill="none" stroke="#3f6fb3" stroke-width="1.4"/>
            <path d="M1.5 7 H12.5 M7 1.5 C4 5 4 9 7 12.5 M7 1.5 C10 5 10 9 7 12.5" fill="none" stroke="#3f6fb3" stroke-width="1.1"/>
          </svg>
          www.VanteluxGear.com
        </li>
        <li class="contact-item">
          <svg class="contact-icon" viewBox="0 0 14 14" aria-hidden="true">
            <path d="M3 1.5 L5.5 1.5 L6.5 4.5 L5 5.7 C5.8 7.5 6.5 8.2 8.3 9 L9.5 7.5 L12.5 8.5 L12.5 11 C12.5 12 11.5 12.7 10.5 12.5 C6 11.5 2.5 8 1.5 3.5 C1.3 2.5 2 1.5 3 1.5 Z" fill="#3f6fb3"/>
          </svg>
          +1 (555) 014-2286
        </li>
      </ul>
    </section>

    <section class="card card-back" aria-label="Business card back">
      <div class="card-surface" role="img" aria-label="Dark faceted low-poly background"></div>
      <div class="brand">
        <span class="brand-mark" aria-hidden="true"></span>
        <span class="brand-name">Vantelux Gear</span>
      </div>
    </section>
  </main>
</body>
</html>
```